Tile Installation business needs a van wrap design using supplied logo

Need wrap designed for a 2023 Bravik Haulmate Compact cargo van with the supplied logos. Looking at all options lettering kits, half wraps, and full wrap designs. We install floor tiles and build new showers, and backsplashes. The final design should catch the eye of someone when driving on the road and not be too cluttered.

```html
<!DOCTYPE html>
<html lang="en">
<head>
<meta charset="utf-8">
<title>Harborline Tile &amp; Stone — Van Wrap</title>
<link rel="stylesheet" href="https://fonts.googleapis.com/css2?family=Roboto:wght@300;700&family=Roboto+Condensed:wght@700&display=swap">
<style>
  :root {
    --paper: #ffffff;
    --green-deep: #0f4a22;
    --green-mid: #1f6e35;
    --green-bright: #3aa548;
    --green-text: #1d6a33;
    --green-contact: #2c8a3b;
    --ink: #1a1a1a;
    --on-green: #ffffff;
  }
  html, body {
    margin: 0;
    padding: 0;
    overflow: hidden;
    background: var(--paper);
  }
  .wrap-canvas {
    position: relative;
    width: 1200px;
    height: 584px;
    overflow: hidden;
    background: var(--paper);
    font-family: "Roboto", Arial, sans-serif;
  }
  .wrap-graphic {
    position: absolute;
    inset: 0;
    width: 1200px;
    height: 584px;
  }
  .contact {
    position: absolute;
    left: 194px;
    top: 292px;
    color: var(--green-contact);
  }
  .contact-phone {
    font-family: "Roboto Condensed", Arial, sans-serif;
    font-weight: 700;
    font-size: 17px;
    letter-spacing: 0.3px;
    margin: 0;
  }
  .contact-web {
    font-family: "Roboto Condensed", Arial, sans-serif;
    font-weight: 700;
    font-size: 7.5px;
    letter-spacing: 0.4px;
    margin: 2px 0 0 4px;
    text-transform: uppercase;
  }
  .brand {
    position: absolute;
    left: 383px;
    top: 298px;
    display: flex;
    align-items: center;
    gap: 12px;
  }
  .brand-square {
    width: 14px;
    height: 14px;
    background: var(--green-mid);
  }
  .brand-name {
    margin: 0;
    font-weight: 300;
    font-size: 30px;
    line-height: 1.1;
    color: var(--ink);
    letter-spacing: 1px;
    text-transform: uppercase;
  }
  .tagline {
    position: absolute;
    left: 636px;
    top: 139px;
    margin: 0;
    font-family: "Roboto Condensed", Arial, sans-serif;
    font-weight: 700;
    font-size: 15px;
    line-height: 16.5px;
    letter-spacing: 0.6px;
    color: var(--green-text);
    text-transform: uppercase;
  }
  .panel-mark {
    position: absolute;
    left: 790px;
    top: 190px;
    display: flex;
    align-items: center;
    gap: 16px;
  }
  .panel-mark-square {
    width: 48px;
    height: 48px;
    background: var(--on-green);
  }
  .panel-mark-name {
    margin: 0;
    font-weight: 700;
    font-size: 28px;
    line-height: 1.1;
    letter-spacing: 1px;
    color: var(--on-green);
    text-transform: uppercase;
  }
</style>
</head>
<body>
<main class="wrap-canvas">
  <svg class="wrap-graphic" viewBox="0 0 1200 584" aria-hidden="true">
    <defs>
      <linearGradient id="band-bright" x1="0" y1="1" x2="1" y2="0">
        <stop offset="0" stop-color="#45b04f"/>
        <stop offset="1" stop-color="#2a8a3c"/>
      </linearGradient>
      <linearGradient id="band-deep" x1="0" y1="0" x2="1" y2="0">
        <stop offset="0" stop-color="#2a7c3b"/>
        <stop offset="1" stop-color="#0c3f1c"/>
      </linearGradient>
    </defs>
    <polygon class="band-bright" points="630,430 858,97 1085,97 1085,430" fill="url(#band-bright)"/>
    <polygon class="band-deep" points="725,300 860,97 1085,97 1085,440 815,440" fill="url(#band-deep)"/>
  </svg>

  <p class="tagline">Expert Tile<br>Installation<br>Services</p>

  <div class="panel-mark" role="img" aria-label="Harborline Tile &amp; Stone brand mark">
    <span class="panel-mark-square"></span>
    <p class="panel-mark-name">Harborline<br>Tile &amp; Stone</p>
  </div>

  <div class="contact">
    <p class="contact-phone">555-014-7392</p>
    <p class="contact-web">harborlinetile.com</p>
  </div>

  <div class="brand">
    <span class="brand-square"></span>
    <p class="brand-name">Harborline<br>Tile &amp; Stone</p>
  </div>
</main>
</body>
</html>
```